Process Engineering/Construction Firm wants a OneSheet targeting craft brewers in Texas

We need a OneSheet (standard letter size) that we can share with craft brewers in our state, that explains what we can do for them. This will be shared primarily via email and online. We would like to see this be fun and modern flyer while still maintaining our professional vibe. More info and logos are uploaded - please review. Also, this project could lead to more branded documents from OneSheets to letterhead. We have our website and our logo(s) and really not much else that is consistent. There is certainly opportunity to work long-term.
Updates

Please note that the website listed on the flyer should read www.halvernworksadvisory.com. It will NOT follow the same domain name as the email address. And also, please DO NOT send me anything through the sales@hwaadvisoryllc.com email address at this time. I am trying to find a brewery-specific photo to use and will upload once found. I will be uploading shortly another logo of an affiliate organization we belong to - the Lone Kettle Brewing Alliance that I would like to see included on the flyer with the words, "A proud member of the Lone Kettle Brewing Alliance' OR just 'Proud Member.'

Target Market(s)

Craft brewery owners in Texas

Industry/Entity Type

Engineering

Font styles to use
Sans Serif

Requirements
Must have
• We need our point of contact to list the website as well as this email: sales@hwaadvisoryllc.com
• Maroon CMYK is: 32, 100, 82, 30
• We want these Brewery Specific service points included:
• • Brewhouse automation
• • Glycol systems
• • Complete line design and install
• • Packaging solutions
• • Epoxy & urethane flooring
• • New construction
• • Network of industry professionals
Nice to have
• Trendy and modern look to correlate with current craft beer logos and design trends

```html
<!DOCTYPE html>
<html lang="en">
<head>
<meta charset="utf-8">
<title>Halvern Works Advisory – Brewery One Sheet</title>
<link rel="stylesheet" href="https://fonts.googleapis.com/css2?family=Montserrat:wght@300;400;500;600;700&display=swap">
<style>
  :root {
    --maroon: #7b1a2b;
    --maroon-deep: #6c1a27;
    --badge-blue: #1d5b97;
    --page-bg: #d9d4c9;
    --services-bg: #e6e6e8;
    --sheet-white: #f6f6f6;
    --ink: #3a3a3d;
    --ink-soft: #8a8a8e;
    --dash: #d9a0a6;
    --white: #ffffff;
  }
  * { box-sizing: border-box; margin: 0; padding: 0; }
  html, body {
    width: 1200px; height: 795px; overflow: hidden;
    background: var(--page-bg);
    font-family: "Montserrat", Arial, sans-serif;
  }
  .sheet {
    position: absolute; left: 306px; top: 17px;
    width: 767px; height: 993px;
    transform: scale(0.765); transform-origin: top left;
    background: var(--sheet-white);
    overflow: hidden;
    box-shadow: 0 2px 6px rgba(0,0,0,0.18);
  }
  .abs { position: absolute; }

  /* Header band */
  .contact-band { left: 0; top: 0; width: 767px; height: 88px; background: var(--maroon-deep); }
  .contact-box {
    top: 25px; width: 253px; height: 37px;
    border: 1.5px solid rgba(255,255,255,0.85);
    color: var(--white); font-size: 14.5px; letter-spacing: 0.6px;
    padding: 13px 0 0 5px; white-space: nowrap;
  }
  .contact-box .label {
    position: absolute; left: 4px; top: -10px; padding: 0 3px;
    background: var(--maroon-deep); font-size: 13.5px; letter-spacing: 1px;
  }
  .contact-web { left: 202px; }
  .contact-email { left: 484px; }

  /* Hero */
  .hero-photo {
    left: 0; top: 88px; width: 767px; height: 340px;
    background:
      radial-gradient(ellipse 120px 170px at 575px 150px, #8a4a16 0%, #5a2c0c 55%, transparent 100%),
      linear-gradient(160deg, #1e1612 0%, #2b1c12 35%, #6b4522 62%, #8c5d2e 78%, #3c2614 100%);
  }
  .member-badge { left: 50px; top: 0; width: 123px; height: 162px; }
  .member-badge .caption {
    position: absolute; top: 11px; width: 123px; text-align: center;
    color: #dfe8f3; font-size: 12px; line-height: 15px; letter-spacing: 0.4px;
  }
  .hero-kicker {
    left: 46px; top: 188px; color: var(--white);
    font-size: 24px; font-weight: 600; letter-spacing: 2.6px;
  }
  .hero-title {
    left: 44px; top: 218px; color: var(--white);
    font-size: 41px; font-weight: 700; letter-spacing: 4px;
  }
  .hero-rule { left: 46px; top: 277px; width: 57px; height: 4px; background: var(--white); }
  .hero-tagline {
    left: 46px; top: 298px; width: 280px; color: var(--white);
    font-size: 13.5px; line-height: 16.5px; letter-spacing: 0.3px;
  }

  /* Services */
  .services { left: 0; top: 428px; width: 767px; height: 378px; background: var(--services-bg); }
  .section-heading { color: var(--ink); font-size: 21px; font-weight: 300; white-space: nowrap; }
  .section-heading strong { font-weight: 600; }
  .heading-rule { height: 5px; background: var(--maroon); }
  .services-heading { left: 0; width: 767px; top: 460px; text-align: center; }
  .services-rule { left: 352px; top: 487px; width: 53px; }

  .service { display: flex; align-items: center; gap: 11px; }
  .service-icon { width: 52px; height: 52px; flex: none; }
  .service-name { color: var(--ink); font-size: 17px; line-height: 21px; font-weight: 300; white-space: nowrap; }
  .service-name strong { font-weight: 600; display: block; }

  .dash-h { height: 0; border-top: 2px dashed var(--dash); }
  .dash-v { width: 0; border-left: 2px dashed var(--dash); }

  .brewery-title {
    left: 57px; top: 688px; color: var(--ink);
    font-size: 21px; line-height: 25px; font-weight: 300;
  }
  .brewery-title strong { font-weight: 600; display: block; }
  .brewery-rule { left: 57px; top: 766px; width: 53px; }
  .checklist { list-style: none; }
  .checklist li {
    display: flex; align-items: center; gap: 7px; height: 22.5px;
    color: var(--ink-soft); font-size: 12.5px; letter-spacing: 0.1px; white-space: nowrap;
  }
  .checklist svg { width: 12px; height: 12px; flex: none; }
  .checklist-left { left: 185px; top: 690px; }
  .checklist-right { left: 444px; top: 690px; }

  /* About */
  .about-heading { top: 834px; }
  .about-rule { top: 861px; width: 54px; }
  .about-copy {
    top: 876px; width: 280px; color: var(--ink-soft);
    font-size: 12px; line-height: 15px; letter-spacing: 0.5px;
  }
  .footer-bar { left: 185px; top: 983px; width: 398px; height: 10px; background: var(--maroon); }
</style>
</head>
<body>
<main class="sheet">

  <div class="abs hero-photo" role="img" aria-label="Photo of a pint of amber craft beer on a rustic wooden bar top in a dim taproom"></div>

  <header class="abs contact-band"></header>
  <div class="abs contact-box contact-web"><span class="label">WEB</span>halvernworksadvisory.com</div>
  <div class="abs contact-box contact-email"><span class="label">EMAIL</span>sales@hwaadvisoryllc.com</div>

  <div class="abs member-badge" aria-label="Proud member of the Lone Kettle Brewing Alliance">
    <svg width="123" height="162" viewBox="0 0 123 162">
      <path d="M0 0 H123 V130 L61.5 162 L0 130 Z" fill="var(--badge-blue)"/>
      <circle cx="61.5" cy="97" r="40" fill="#e9eef5"/>
      <circle cx="61.5" cy="97" r="32" fill="var(--badge-blue)"/>
    </svg>
    <p class="caption">PROUD<br>MEMBER OF</p>
  </div>

  <p class="abs hero-kicker">HALVERN WORKS</p>
  <h1 class="abs hero-title">ADVISORY</h1>
  <div class="abs hero-rule"></div>
  <p class="abs hero-tagline">Providing precision engineering and construction solutions to industries across the U.S</p>

  <section class="abs services"></section>
  <h2 class="abs section-heading services-heading">OUR <strong>SERVICES</strong></h2>
  <div class="abs heading-rule services-rule"></div>

  <div class="abs dash-v" style="left:252px; top:508px; height:140px;"></div>
  <div class="abs dash-v" style="left:482px; top:508px; height:140px;"></div>
  <div class="abs dash-h" style="left:54px; top:577px; width:170px;"></div>
  <div class="abs dash-h" style="left:281px; top:577px; width:176px;"></div>
  <div class="abs dash-h" style="left:506px; top:577px; width:184px;"></div>

  <div class="abs service" style="left:54px; top:511px;">
    <svg class="service-icon" viewBox="0 0 52 52"><circle cx="26" cy="26" r="26" fill="var(--maroon)"/><g fill="none" stroke="#fff" stroke-width="1.4"><circle cx="26" cy="17" r="4"/><path d="M19 28 a7 6 0 0 1 14 0"/><circle cx="17" cy="31" r="3"/><circle cx="35" cy="31" r="3"/><path d="M11 40 a6 5 0 0 1 12 0 M29 40 a6 5 0 0 1 12 0"/></g></svg>
    <p class="service-name">Project<strong>Consulting</strong></p>
  </div>
  <div class="abs service" style="left:281px; top:511px;">
    <svg class="service-icon" viewBox="0 0 52 52"><circle cx="26" cy="26" r="26" fill="var(--maroon)"/><g fill="none" stroke="#fff" stroke-width="1.4"><rect x="14" y="14" width="24" height="24"/><path d="M18 20 H34 M21 25 H34 M21 30 H30 M18 34 H34"/></g></svg>
    <p class="service-name">Project<strong>Management</strong></p>
  </div>
  <div class="abs service" style="left:505px; top:511px;">
    <svg class="service-icon" viewBox="0 0 52 52"><circle cx="26" cy="26" r="26" fill="var(--maroon)"/><g fill="none" stroke="#fff" stroke-width="1.4"><rect x="15" y="15" width="22" height="14"/><path d="M26 15 V29"/><circle cx="16" cy="35" r="2"/><circle cx="21" cy="35" r="2"/><circle cx="26" cy="35" r="2"/><circle cx="31" cy="35" r="2"/><circle cx="36" cy="35" r="2"/></g></svg>
    <p class="service-name">Process<strong>Engineering</strong></p>
  </div>
  <div class="abs service" style="left:54px; top:591px;">
    <svg class="service-icon" viewBox="0 0 52 52"><circle cx="26" cy="26" r="26" fill="var(--maroon)"/><g fill="none" stroke="#fff" stroke-width="1.4"><circle cx="26" cy="26" r="13" stroke-dasharray="4 2"/><circle cx="26" cy="26" r="7"/><circle cx="26" cy="26" r="2.5"/></g></svg>
    <p class="service-name">Automation<strong>Engineering</strong></p>
  </div>
  <div class="abs service" style="left:281px; top:591px;">
    <svg class="service-icon" viewBox="0 0 52 52"><circle cx="26" cy="26" r="26" fill="var(--maroon)"/><g fill="none" stroke="#fff" stroke-width="1.6"><circle cx="23" cy="23" r="9"/><path d="M29.5 29.5 L38 38"/><path d="M19 23 L22 26 L27 20"/></g></svg>
    <p class="service-name">Manufacturing<strong>Optimization</strong></p>
  </div>
  <div class="abs service" style="left:505px; top:591px;">
    <svg class="service-icon" viewBox="0 0 52 52"><circle cx="26" cy="26" r="26" fill="var(--maroon)"/><g fill="none" stroke="#fff" stroke-width="1.4"><path d="M14 38 L38 14 V38 Z"/><path d="M25 38 V34 M30 38 V35 M35 38 V34 M33 29 L33 33 L29 33 Z"/></g></svg>
    <p class="service-name">Construction and<strong>Industrial Flooring</strong></p>
  </div>

  <h2 class="abs brewery-title">Brewery<strong>Specific</strong><strong>Services</strong></h2>
  <div class="abs heading-rule brewery-rule"></div>

  <ul class="abs checklist checklist-left">
    <li><svg viewBox="0 0 12 12"><rect x="0.75" y="0.75" width="10.5" height="10.5" fill="none" stroke="var(--maroon)" stroke-width="1.5"/><path d="M3 6 L5.3 8.3 L11 2" fill="none" stroke="var(--maroon)" stroke-width="1.8"/></svg>BREWHOUSE AUTOMATION</li>
    <li><svg viewBox="0 0 12 12"><rect x="0.75" y="0.75" width="10.5" height="10.5" fill="none" stroke="var(--maroon)" stroke-width="1.5"/><path d="M3 6 L5.3 8.3 L11 2" fill="none" stroke="var(--maroon)" stroke-width="1.8"/></svg>GLYCOL SYSTEMS</li>
    <li><svg viewBox="0 0 12 12"><rect x="0.75" y="0.75" width="10.5" height="10.5" fill="none" stroke="var(--maroon)" stroke-width="1.5"/><path d="M3 6 L5.3 8.3 L11 2" fill="none" stroke="var(--maroon)" stroke-width="1.8"/></svg>EPOXY &amp; URETHANE FLOORING</li>
    <li><svg viewBox="0 0 12 12"><rect x="0.75" y="0.75" width="10.5" height="10.5" fill="none" stroke="var(--maroon)" stroke-width="1.5"/><path d="M3 6 L5.3 8.3 L11 2" fill="none" stroke="var(--maroon)" stroke-width="1.8"/></svg>NEW CONSTRUCTION</li>
  </ul>
  <ul class="abs checklist checklist-right">
    <li><svg viewBox="0 0 12 12"><rect x="0.75" y="0.75" width="10.5" height="10.5" fill="none" stroke="var(--maroon)" stroke-width="1.5"/><path d="M3 6 L5.3 8.3 L11 2" fill="none" stroke="var(--maroon)" stroke-width="1.8"/></svg>COMPLETE LINE DESIGN AND INSTALL</li>
    <li><svg viewBox="0 0 12 12"><rect x="0.75" y="0.75" width="10.5" height="10.5" fill="none" stroke="var(--maroon)" stroke-width="1.5"/><path d="M3 6 L5.3 8.3 L11 2" fill="none" stroke="var(--maroon)" stroke-width="1.8"/></svg>PACKAGING SOLUTIONS</li>
    <li><svg viewBox="0 0 12 12"><rect x="0.75" y="0.75" width="10.5" height="10.5" fill="none" stroke="var(--maroon)" stroke-width="1.5"/><path d="M3 6 L5.3 8.3 L11 2" fill="none" stroke="var(--maroon)" stroke-width="1.8"/></svg>NETWORK OF INDUSTRY PROFESSIONALS</li>
  </ul>

  <h2 class="abs section-heading about-heading" style="left:56px;">WHO <strong>WE ARE?</strong></h2>
  <div class="abs heading-rule about-rule" style="left:56px;"></div>
  <p class="abs about-copy" style="left:56px;">With a policy of recruiting only the highest caliber members and supporting continued professional development, HWA ensures that it remains at the forefront of technological capabilities</p>

  <div class="abs dash-v" style="left:383px; top:830px; height:130px;"></div>

  <h2 class="abs section-heading about-heading" style="left:449px;">WHAT <strong>WE DO?</strong></h2>
  <div class="abs heading-rule about-rule" style="left:449px;"></div>
  <p class="abs about-copy" style="left:449px; width:265px;">The Halvern Works Advisory team not only understands what it takes to deliver for multi-national corporations, but also the unique needs of smaller companies, engineering firms, and municipalities.</p>

  <div class="abs footer-bar"></div>
</main>
</body>
</html>
```